Gutschein-Design für Verkauf von hochwertigem Bisonfleisch
Zielgruppe
Das Unternehmen verkauft sehr hochwertiges, kanadisches Bisonfleisch über den Online-Shop (weidenkorn.de). Die Zielgruppe sind weitestgehend Männer mit entsprechendem Einkommen.
Aufgabenstellung
Die Karte soll ein solches Maß haben, dass es in einen breiten Briefumschlag DIN Lang rein passt. Sie soll von beiden Seiten bunt bedruckt sein. Die Karte soll als Geschenkgutschein, z.B. zu Weihnachten verwendet werden. Das Design soll möglichst schörkellos sein und die Natur und das Tier in den Vordergrund stellen. Fleisch, z.B. Grillfleisch, soll nicht zu sehen sein.

```html
<!DOCTYPE html>
<html lang="de">
<head>
<meta charset="utf-8">
<title>Weidenkorn Gutschein</title>
<link href="https://fonts.googleapis.com/css2?family=Bodoni+Moda:wght@400;500;700&display=swap" rel="stylesheet">
<style>
  :root {
    --page: #ededed;
    --card: #ffffff;
    --gold: #c6a577;
    --band: #5a5a5a;
    --ink: #2b2b2b;
    --field-ink: #4a4a4a;
    --footer-ink: #ffffff;
  }
  * { margin: 0; padding: 0; box-sizing: border-box; }
  html, body { width: 1200px; height: 1081px; overflow: hidden; background: var(--page); }
  body { position: relative; font-family: "Bodoni Moda", "Times New Roman", serif; color: var(--ink); }

  .card {
    position: absolute; left: 148px; width: 908px; height: 424px;
    background: var(--card);
    box-shadow: 0 4px 14px rgba(0,0,0,0.12);
    overflow: hidden;
  }
  .card--front { top: 69px; }
  .card--back { top: 584px; left: 147px; }

  /* front */
  .front-photo {
    position: absolute; left: 17px; top: 18px; width: 874px; height: 325px;
    background: linear-gradient(180deg, #c9d4e0 0%, #e9eef3 22%, #8f9fb4 48%, #6f7f99 58%, #c99a3c 62%, #d4a84e 80%, #b88a33 100%);
  }
  .brand-box {
    position: absolute; left: 679px; top: 18px; width: 170px; height: 113px;
    background: rgba(255,255,255,0.88);
    display: flex; align-items: center; justify-content: center;
  }
  .brand-name { font-weight: 700; font-size: 19px; letter-spacing: 0.5px; color: #1f1f1f; }
  .title-band {
    position: absolute; left: 17px; top: 343px; width: 874px; height: 65px;
    background: var(--band);
  }
  .title-band .title { position: absolute; left: 0; right: 0; top: 6px; text-align: center; }
  .title-band svg { position: absolute; left: 0; top: 0; }
  .title {
    font-size: 52px; font-weight: 400; color: var(--gold); letter-spacing: 0.5px; line-height: 1;
  }

  /* back */
  .back-photo {
    position: absolute; inset: 0;
    background: linear-gradient(180deg, #f6f7f9 0%, #eceff3 20%, #dfe3ea 42%, #d3d7de 58%, #e3e5e9 72%, #eceef1 86%, #f4f5f7 100%);
  }
  .back-title { position: absolute; left: 0; right: 0; top: 46px; text-align: center; }
  .field {
    position: absolute; left: 248px; width: 411px; height: 39px;
    background: #ffffff; padding: 5px 7px;
    font-size: 10px; color: var(--field-ink); letter-spacing: 0.3px;
  }
  .field--value { top: 114px; }
  .field--recipient { top: 166px; }
  .field--number { top: 217px; }
  .redeem {
    position: absolute; left: 0; right: 0; top: 276px; text-align: center;
    font-size: 11px; color: var(--field-ink); letter-spacing: 0.3px;
  }
  .footer-band {
    position: absolute; left: 0; right: 0; bottom: 0; height: 39px;
    background: var(--gold);
    display: flex; align-items: center; justify-content: space-between; padding: 0 22px;
    font-size: 12px; color: var(--footer-ink); letter-spacing: 0.2px; text-transform: uppercase;
  }
</style>
</head>
<body>
  <section class="card card--front">
    <div class="front-photo" role="img" aria-label="Bison im goldenen Präriegras vor schneebedeckten Bergen"></div>
    <div class="brand-box"><span class="brand-name">WEIDENKORN</span></div>
    <div class="title-band">
      <svg width="874" height="65" aria-hidden="true">
        <g stroke="#c6a577" stroke-width="1.2" fill="#c6a577">
          <line x1="135" y1="33" x2="262" y2="33"/>
          <line x1="612" y1="33" x2="739" y2="33"/>
          <circle cx="165" cy="33" r="1.8"/>
          <circle cx="709" cy="33" r="1.8"/>
        </g>
      </svg>
      <div class="title">GUTSCHEIN</div>
    </div>
  </section>

  <section class="card card--back">
    <div class="back-photo" role="img" aria-label="Bisonherde in verschneiter Berglandschaft"></div>
    <div class="back-title title">GUTSCHEIN</div>
    <div class="field field--value">IM WERT VON</div>
    <div class="field field--recipient">FÜR</div>
    <div class="field field--number">GUTSCHEIN-NR.</div>
    <p class="redeem">EINZULÖSEN AUF WWW.WEIDENKORN.DE/SHOP</p>
    <footer class="footer-band">
      <span>Weidenkorn UG</span>
      <span>Am Lindenhang 14</span>
      <span>37520 Talbrunn</span>
      <span>05300-4471820</span>
      <span>info@weidenkorn.de</span>
      <span>www.weidenkorn.de</span>
    </footer>
  </section>
</body>
</html>
```